Recruitment Package Design for Healthcare Organization

We need a brochure designed that matches the design of our website and logo. The focus of the brochure is to provide information about our organization and region to prospective physicians looking to join our team. I have the content already put together, but would like some imagery of local geography/activities to be incorporated into the design. I have attached the content document as well as an example we are wanting to model ours after.

Our website is: https://brightoakclinicgroup.ca/

Target Market(s)

Prospective physicians

Industry/Entity Type

Healthcare

Requirements
Must have
• Local imagery which I have attached.

```html
<!DOCTYPE html>
<html lang="en">
<head>
<meta charset="utf-8">
<title>Brightoak Clinic Group – Brochure Cover</title>
<link href="https://fonts.googleapis.com/css2?family=Questrial&family=Mulish:wght@800&display=swap" rel="stylesheet">
<style>
  :root{
    --stage:#8a8a8a;
    --teal:#2aaab8;
    --teal-bright:#33bccb;
    --paper:#f1f1f1;
    --slate:#5e6164;
    --mist:#cdd3db;
    --ink-grey:#6b6d70;
    --white:#ffffff;
  }
  *{margin:0;padding:0;box-sizing:border-box}
  html,body{width:1200px;height:1200px;overflow:hidden;background:var(--stage)}
  .spread{position:absolute;left:140px;top:275px;width:920px;height:650px;display:flex;box-shadow:0 18px 40px rgba(0,0,0,.25)}
  .page{position:relative;width:460px;height:650px;overflow:hidden}

  /* back cover */
  .back-cover{background:var(--teal)}
  .brand-box{position:absolute;left:176px;top:18px;width:232px;height:150px;background:var(--paper);display:flex;align-items:center;justify-content:center;gap:12px}
  .brand-mark{width:26px;height:26px;border-radius:50%;background:var(--teal);flex:none}
  .brand-name{font-family:"Questrial",sans-serif;color:var(--teal);font-size:26px;line-height:1.05}
  .spine-bar{position:absolute;left:404px;width:30px;background:var(--slate);outline:6px solid var(--paper)}
  .spine-bar.upper{top:72px;height:278px}
  .spine-bar.lower{top:440px;height:220px}
  .location{position:absolute;left:62px;top:205px;color:var(--white)}
  .location-title{font-family:"Mulish",sans-serif;font-weight:800;font-size:24px;display:flex;align-items:center;gap:8px;margin-bottom:14px}
  .location-list{list-style:none;font-family:"Questrial",sans-serif;font-size:12.5px;line-height:1.45;width:300px}
  .web{display:flex;align-items:center;gap:8px;margin-top:14px;font-family:"Mulish",sans-serif;font-weight:800;font-size:16px}

  /* front cover */
  .front-cover{background:var(--paper)}
  .edge-strip{position:absolute;left:0;top:0;width:8px;height:100%;background:var(--paper)}
  .teal-column{position:absolute;left:8px;top:0;width:104px;height:100%;background:var(--teal-bright)}
  .cross-band{position:absolute;left:-2px;top:350px;width:10px;height:90px;background:var(--teal-bright)}
  .photo-band{position:absolute;left:112px;top:478px;width:318px;height:48px;background:var(--teal-bright)}
  .mist-shape{position:absolute;right:-60px;top:300px;width:150px;height:150px;background:var(--mist);border-radius:26px;transform:rotate(45deg)}
  .front-brand{position:absolute;right:40px;top:110px;display:flex;align-items:center;gap:14px}
  .front-brand .brand-name{font-size:30px}
  .photo{position:absolute;left:116px;top:225px;width:300px;height:300px}
  .tagline{position:absolute;left:128px;top:560px;font-family:"Mulish",sans-serif;font-weight:800;font-size:25px;line-height:1.1;color:var(--teal-bright)}
</style>
</head>
<body>
<main class="spread">
  <section class="page back-cover">
    <div class="brand-box">
      <span class="brand-mark"></span>
      <span class="brand-name">brightoak<br>clinic group</span>
    </div>
    <div class="spine-bar upper"></div>
    <div class="spine-bar lower"></div>
    <div class="location">
      <h2 class="location-title">
        <svg width="16" height="20" viewBox="0 0 16 20"><path d="M8 0a7 7 0 0 0-7 7c0 5 7 13 7 13s7-8 7-13a7 7 0 0 0-7-7z" fill="#fff"/><circle cx="8" cy="7" r="2.6" fill="#2aaab8"/></svg>
        Location
      </h2>
      <ul class="location-list">
        <li>Northvale – Harbourside (Family Practice)</li>
        <li>Northvale – Elmwood (Cedar Ridge Family Medicine &amp; Maternity)</li>
        <li>Northvale – Glenhaven (Hilltop)</li>
        <li>Northvale – Harbourside (Sports Medicine)</li>
        <li>Lakeview (Pine Cove Medical Clinic)</li>
        <li>Northvale – (Women's Wellness – Contraceptive Clinic)</li>
        <li>Northvale – Elmwood</li>
      </ul>
      <p class="web">
        <svg width="18" height="18" viewBox="0 0 18 18" fill="none" stroke="#fff" stroke-width="1.2"><circle cx="9" cy="9" r="8"/><ellipse cx="9" cy="9" rx="3.5" ry="8"/><path d="M1 9h16M2.5 5h13M2.5 13h13"/></svg>
        www.brightoakclinicgroup.ca
      </p>
    </div>
  </section>

  <section class="page front-cover">
    <div class="teal-column"></div>
    <div class="edge-strip"></div>
    <div class="cross-band"></div>
    <div class="mist-shape"></div>
    <div class="photo-band"></div>
    <div class="front-brand">
      <span class="brand-mark"></span>
      <span class="brand-name">brightoak<br>clinic group</span>
    </div>
    <svg class="photo" viewBox="0 0 300 300" role="img" aria-label="Photo of a clinician listening to an older patient's chest with a stethoscope at home">
      <defs>
        <linearGradient id="photoTones" x1="0" y1="0" x2="1" y2="1">
          <stop offset="0" stop-color="#9fb9cf"/>
          <stop offset=".5" stop-color="#d9d2c6"/>
          <stop offset="1" stop-color="#b9bfc6"/>
        </linearGradient>
      </defs>
      <rect x="44" y="44" width="212" height="212" rx="30" transform="rotate(45 150 150)" fill="url(#photoTones)" stroke="#5e6164" stroke-width="7"/>
    </svg>
    <p class="tagline">Your partner in health.<br>Your partner in life.</p>
  </section>
</main>
</body>
</html>
```